Harbor Nest Lodging website, brand new company, that rents rooms out in houses to milleniuls

We have a site right now that is weak as heck! We could use some punching it up. So we want it to be fun and cool, with added items in for social media (just chirpnet now) and anything else you want to throw at us. We do have a “blog” in there dedicated to events (we throw a lot of them) so want to incorporate that. Also have an existing design for a hand out that we want to use as our launching pad for colors… you can deviate from it a bit though.

Target Market(s)

25-40 year olds transitioning to the city from other places in the country. Millennial are the min group

Industry/Entity Type

Real Estate

Coding

Coded - Design and coding required

Number of Pages Required

5+ page

Font styles to use
Sans Serif

Requirements
Must have
• Fun look, same pages as those uploaded, but not necessarily the look and feel of what we have already.
• Follow the content of our posted site www.HarborNestLodging.example
• FOOTER
• LOGO | SITEMAP | SOCIAL LINKS | MAIN CTA REMINDER | CONTACT INFO | COPYRIGHT INFO | TERMS AND CONDITIONS
Nice to have
• Use as many of my graphics as loaded, but feel free to use stock photos as well interlaced. Including both people in their 20’s, 30’s, 40’s, having a fun time or of nice houses, inside and out.

```html
<!DOCTYPE html>
<html lang="en">
<head>
<meta charset="utf-8">
<title>Harbor Nest Lodging</title>
<link rel="stylesheet" href="https://fonts.googleapis.com/css2?family=Montserrat:wght@400;500;600;700&family=Open+Sans:wght@400;600&display=swap">
<style>
  :root {
    --blue: #1f56b0;
    --blue-deep: #17449a;
    --blue-light: #3a73cc;
    --green: #66ac2a;
    --green-dark: #559521;
    --grey-panel: #ececec;
    --grey-border: #d3d3d3;
    --grey-band: #e6e6e6;
    --ink: #333333;
    --footer: #1b1b1b;
    --footer-muted: #bdbdbd;
    --social: #4a4a4a;
    --chirpnet: #2aa3e6;
    --white: #ffffff;
  }
  * { margin: 0; padding: 0; box-sizing: border-box; }
  html, body { width: 1200px; height: 3114px; overflow: hidden; background: var(--white); }
  body { font-family: "Open Sans", Arial, sans-serif; color: var(--ink); }
  .page { position: relative; width: 1200px; height: 3114px; overflow: hidden; }

  /* Header + hero */
  .hero-bg { position: absolute; left: 0; top: 0; width: 1200px; height: 780px; }
  .brand { position: absolute; top: 64px; left: 0; width: 1200px; text-align: center;
    font-family: "Montserrat", sans-serif; font-weight: 700; font-size: 42px; letter-spacing: 1px;
    color: var(--white); text-transform: uppercase; line-height: 1; }
  .main-nav { position: absolute; top: 176px; left: 0; width: 1200px; height: 52px; background: var(--green);
    display: flex; justify-content: center; align-items: center; gap: 62px; }
  .main-nav a { font-family: "Montserrat", sans-serif; font-weight: 600; font-size: 14px; color: var(--white);
    text-decoration: none; text-transform: uppercase; letter-spacing: .3px; }
  .hero-title { position: absolute; top: 324px; left: 0; width: 1200px; text-align: center; color: var(--white); }
  .hero-title h1 { font-family: "Montserrat", sans-serif; font-weight: 700; font-size: 58px; letter-spacing: 1px; line-height: 1; }
  .hero-title .sub { display: inline-flex; align-items: center; gap: 14px; margin-top: 14px;
    font-family: "Montserrat", sans-serif; font-weight: 400; font-size: 32px; letter-spacing: 1px; }
  .hero-title .sub::before, .hero-title .sub::after { content: ""; width: 86px; height: 2px; background: var(--white); }
  .hero-arrow { position: absolute; top: 346px; }
  .hero-arrow.prev { left: 30px; } .hero-arrow.next { right: 30px; }
  .moment { position: absolute; border-radius: 50%; border: 9px solid var(--green);
    background: radial-gradient(circle at 45% 40%, #a78a74, #4f4a52 70%, #2d3040); }

  /* Intro boxes */
  .info-box { position: absolute; top: 826px; width: 494px; height: 392px; background: var(--grey-panel);
    border: 1px solid var(--grey-border); padding: 14px 22px; }
  .info-box.left { left: 81px; } .info-box.right { left: 623px; }
  .box-title { font-family: "Montserrat", sans-serif; font-weight: 500; font-size: 23px; color: var(--green);
    text-transform: uppercase; padding-bottom: 6px; border-bottom: 2px solid var(--blue); margin: 0 -8px 18px; padding-left: 8px; }
  .info-box p { font-size: 14.5px; line-height: 27px; margin-bottom: 27px; }
  .amenities { list-style: none; }
  .amenities li { font-size: 14px; line-height: 19px; margin-bottom: 11px; padding-left: 20px; position: relative; }
  .amenities li::before { content: "-"; position: absolute; left: 4px; }
  .cta { position: absolute; top: 1270px; left: 440px; width: 322px; height: 71px; background: var(--green);
    color: var(--white); font-family: "Montserrat", sans-serif; font-weight: 600; font-size: 20px;
    display: flex; align-items: center; justify-content: center; text-transform: uppercase; text-decoration: none; }

  /* Blog band */
  .blog-band { position: absolute; top: 1383px; left: 0; width: 1200px; height: 616px;
    background: linear-gradient(180deg, var(--blue-deep), var(--blue) 50%, var(--blue-deep)); }
  .post { position: absolute; top: 105px; width: 321px; height: 412px; background: var(--white); padding: 18px 14px; }
  .post h3 { font-family: "Montserrat", sans-serif; font-weight: 600; font-size: 19px; color: var(--green);
    text-transform: uppercase; padding: 0 0 8px 4px; border-bottom: 2px solid var(--blue); margin: 0 -2px 14px; }
  .post .thumb { width: 292px; height: 146px; background: linear-gradient(135deg, #7b4b3e, #3a2e38 55%, #b04a3c); }
  .post p { font-size: 13.5px; line-height: 26px; margin: 18px 0 12px; height: 104px; overflow: hidden; }
  .read-more { display: inline-block; background: var(--green); color: var(--white); font-family: "Montserrat", sans-serif;
    font-weight: 700; font-size: 11px; padding: 10px 18px; text-transform: uppercase; text-decoration: none; letter-spacing: .5px; }

  /* Gallery */
  .gallery-shot { position: absolute; top: 2070px; width: 243px; height: 222px; }
  .slide-tab { position: absolute; top: 2146px; width: 30px; height: 60px; background: #3a3a3a;
    display: flex; align-items: center; justify-content: center; }

  /* Fans */
  .fans { position: absolute; top: 2379px; left: 0; width: 1200px; height: 426px; background: var(--grey-band); }
  .fans h2 { position: absolute; top: 32px; left: 255px; width: 690px; display: flex; align-items: center; gap: 18px;
    font-family: "Montserrat", sans-serif; font-weight: 600; font-size: 31px; color: var(--blue); text-transform: uppercase; }
  .fans h2::before, .fans h2::after { content: ""; flex: 1; height: 1px; background: #9aa8c0; }
  .quote { position: absolute; top: 123px; left: 310px; width: 600px; text-align: center; font-family: Arial, sans-serif;
    font-size: 15.5px; line-height: 23px; color: #4a5c86; }
  .quote .mark { position: absolute; left: -28px; top: -4px; font-size: 30px; color: #555; font-family: Georgia, serif; }
  .quote cite { display: block; margin-top: 8px; font-size: 11px; color: #888; }
  .fan-arrow { position: absolute; top: 142px; }
  .avatar { position: absolute; border-radius: 50%; background: radial-gradient(circle at 50% 40%, #c7a48c, #5f7fa3); }
  .avatar.main { left: 542px; top: 266px; width: 116px; height: 116px; border: 5px solid var(--green); }
  .avatar.side { width: 44px; height: 44px; top: 331px; opacity: .75; }

  /* Footer */
  .site-footer { position: absolute; top: 2805px; left: 0; width: 1200px; height: 309px; background: var(--footer); color: var(--white); text-align: center; }
  .footer-brand { padding-top: 34px; font-family: "Montserrat", sans-serif; font-weight: 700; font-size: 26px; line-height: 32px; color: var(--blue-light); text-transform: uppercase; letter-spacing: 1px; }
  .footer-nav { margin-top: 26px; display: flex; justify-content: center; font-family: "Montserrat", sans-serif; font-size: 12.5px; }
  .footer-nav a { color: var(--white); text-decoration: none; text-transform: uppercase; padding: 0 22px; border-left: 1px solid var(--white); line-height: 13px; }
  .footer-nav a:first-child { border-left: none; }
  .footer-reminder { margin-top: 22px; display: flex; justify-content: center; align-items: center; gap: 18px;
    font-family: "Open Sans", sans-serif; font-size: 13px; color: var(--footer-muted); }
  .footer-reminder .reminder-cta { background: var(--green); color: var(--white); text-decoration: none;
    font-family: "Montserrat", sans-serif; font-weight: 600; font-size: 12px; text-transform: uppercase; padding: 8px 18px; }
  .copyright { margin-top: 20px; font-family: Arial, sans-serif; font-size: 12.5px; }
  .copyright a { color: var(--white); text-decoration: underline; margin-left: 10px; }
  .social { margin-top: 22px; display: flex; justify-content: center; gap: 10px; }
  .social a { height: 26px; padding: 0 10px; background: var(--social); display: flex; align-items: center;
    font-family: "Montserrat", sans-serif; font-weight: 500; font-size: 11px; color: var(--white); text-decoration: none; }
  .social a.chirpnet { background: var(--chirpnet); }
</style>
</head>
<body>
<div class="page">

  <svg class="hero-bg" viewBox="0 0 1200 780" role="img" aria-label="Blue-tinted photo of a tree-lined neighbourhood street">
    <defs>
      <linearGradient id="heroTone" x1="0" y1="0" x2="0" y2="1">
        <stop offset="0" stop-color="#1a4ea8"/>
        <stop offset=".5" stop-color="#2461bd"/>
        <stop offset="1" stop-color="#1d55b0"/>
      </linearGradient>
    </defs>
    <path d="M0 0 H1200 V600 Q600 730 0 600 Z" fill="url(#heroTone)"/>
    <path d="M0 600 Q600 730 1200 600" fill="none" stroke="#66ac2a" stroke-width="10"/>
  </svg>

  <div class="brand">Harbor Nest Lodging</div>

  <nav class="main-nav">
    <a href="#">Welcome</a><a href="#">Our Communities</a><a href="#">Ammenities</a><a href="#">Fitting</a><a href="#">Events</a><a href="#">About Us</a><a href="#">Contact</a>
  </nav>

  <svg class="hero-arrow prev" width="18" height="30" viewBox="0 0 18 30"><path d="M15 2 L3 15 L15 28" fill="none" stroke="#fff" stroke-width="3"/></svg>
  <svg class="hero-arrow next" width="18" height="30" viewBox="0 0 18 30"><path d="M3 2 L15 15 L3 28" fill="none" stroke="#fff" stroke-width="3"/></svg>

  <div class="hero-title">
    <h1>PROFESSIONAL</h1>
    <div class="sub">BUILT COMMUNITIES</div>
  </div>

  <div class="moment" role="img" aria-label="Residents sharing a meal" style="left:135px;top:565px;width:142px;height:142px"></div>
  <div class="moment" role="img" aria-label="Group outing in the snow" style="left:305px;top:575px;width:158px;height:158px"></div>
  <div class="moment" role="img" aria-label="Residents posing together outdoors" style="left:495px;top:572px;width:198px;height:198px"></div>
  <div class="moment" role="img" aria-label="Friends at a community party" style="left:735px;top:575px;width:158px;height:158px"></div>
  <div class="moment" role="img" aria-label="Team in helmets on an adventure day" style="left:918px;top:551px;width:144px;height:144px"></div>

  <section class="info-box left">
    <h2 class="box-title">Experience the Difference</h2>
    <p>Traditional apartments and housing rentals are a thing of the past. We have created an all-encompassing living experience that aligns perfectly with your trendy, yet sophisticated lifestyle. Harbor Nest Lodging is unlike anything you have ever experienced before.</p>
    <p>We invite you to explore our selection of home communities and discover the passion we have for providing wonderful experiences.</p>
  </section>

  <section class="info-box right">
    <h2 class="box-title">Luxurious Amenities*</h2>
    <ul class="amenities">
      <li>High-speed Wi-Fi</li>
      <li>All inclusive utilities (with Verdant Link)</li>
      <li>Optional enclosed garage</li>
      <li>Fully furnished kitchen</li>
      <li>Washer and dryer</li>
      <li>Spacious, newly updated rooms</li>
      <li>Private use, full bath with each room</li>
      <li>Bi-monthly community events</li>
      <li>Various networking event invitations, well suited for young professionals</li>
    </ul>
  </section>

  <a class="cta" href="#">Contact Us</a>

  <section class="blog-band">
    <article class="post" style="left:83px">
      <h3>@ Home with HNL</h3>
      <div class="thumb" role="img" aria-label="Friends gathered at a pub table"></div>
      <p>After an exhausting day in the office, the thought of hanging out with co workers is the last thing on your mind. But who says you have to conquer a crowded pub…</p>
      <a class="read-more" href="#">Read More &gt;&gt;</a>
    </article>
    <article class="post" style="left:436px">
      <h3>Most Recent Events</h3>
      <div class="thumb" role="img" aria-label="Residents celebrating at a library event"></div>
      <p>HNL hosts a number of regular events as well as occasional get togethers. All in efforts of bringing each one of our micro-communities together…</p>
      <a class="read-more" href="#">Read More &gt;&gt;</a>
    </article>
    <article class="post" style="left:799px">
      <h3>Our Latest Addition</h3>
      <div class="thumb" role="img" aria-label="Friends gathered at a pub table"></div>
      <p>We are constantly searching for a uniquely beautiful space to create a new community. Check out our latest addition to the family with it's custom finishes and artisan design…</p>
      <a class="read-more" href="#">Read More &gt;&gt;</a>
    </article>
  </section>

  <div class="slide-tab" style="left:0"><svg width="10" height="16" viewBox="0 0 10 16"><path d="M8 2 L2 8 L8 14" fill="none" stroke="#fff" stroke-width="2"/></svg></div>
  <div class="slide-tab" style="right:0"><svg width="10" height="16" viewBox="0 0 10 16"><path d="M2 2 L8 8 L2 14" fill="none" stroke="#fff" stroke-width="2"/></svg></div>
  <div class="gallery-shot" role="img" aria-label="Bright living room with sofa and rug" style="left:81px;background:linear-gradient(180deg,#d9d6cf,#a79b8a 60%,#7a5a3e)"></div>
  <div class="gallery-shot" role="img" aria-label="Front of a white house with porch and trees" style="left:343px;background:linear-gradient(180deg,#6a9ad0,#6f8b55 45%,#c8c7c0)"></div>
  <div class="gallery-shot" role="img" aria-label="Dining room with patterned rug" style="left:610px;background:linear-gradient(180deg,#e3e1dc,#8b8fa0 60%,#3d4a6e)"></div>
  <div class="gallery-shot" role="img" aria-label="Kitchen with wood cabinets and pendant lights" style="left:874px;background:linear-gradient(180deg,#a0643c,#d39b62 55%,#8a5a34)"></div>

  <section class="fans">
    <h2>Our Fans</h2>
    <svg class="fan-arrow" style="left:108px" width="14" height="24" viewBox="0 0 14 24"><path d="M12 2 L3 12 L12 22" fill="none" stroke="#b5b5b5" stroke-width="3"/></svg>
    <svg class="fan-arrow" style="right:108px" width="14" height="24" viewBox="0 0 14 24"><path d="M2 2 L11 12 L2 22" fill="none" stroke="#b5b5b5" stroke-width="3"/></svg>
    <blockquote class="quote">
      <span class="mark">&ldquo;</span>
      Lorem ipsum dolor sit amet, consectetur adipiscing elit, sed do eiusmod tempor incididunt ut labore et dolore magna aliqua. Ut enim ad minim veniam, quis nostrud exercitation ullamco laboris nisi ut aliquip ex ea commodo consequat. Duis aute irure dolor in reprehenderit in voluptate velit esse cillum dolore eu fugiat nulla pariatur.
      <cite>— Someone famous</cite>
    </blockquote>
    <div class="avatar side" role="img" aria-label="Resident portrait" style="left:487px"></div>
    <div class="avatar main" role="img" aria-label="Featured resident portrait"></div>
    <div class="avatar side" role="img" aria-label="Resident portrait" style="left:671px"></div>
  </section>

  <footer class="site-footer">
    <div class="footer-brand">Harbor Nest Lodging</div>
    <nav class="footer-nav">
      <a href="#">Welcome</a><a href="#">Our Communities</a><a href="#">Ammenities</a><a href="#">Fitting</a><a href="#">Events</a><a href="#">About Us</a><a href="#">Contact</a>
    </nav>
    <div class="footer-reminder">
      <span>Ready to find your room?</span>
      <a class="reminder-cta" href="#">Contact Us</a>
      <span>(555) 010-0142 · hello@harbornestlodging.example</span>
    </div>
    <p class="copyright">Copyright © 2016 Harbor Nest Lodging. Right Reserved.<a href="#">Terms &amp; Conditions</a></p>
    <div class="social">
      <a href="#">Mingle</a>
      <a href="#" class="chirpnet">chirpnet</a>
      <a href="#">Circlr</a>
      <a href="#">Snapframe</a>
    </div>
  </footer>

</div>
</body>
</html>
```